SKILLSTEP is a training facility that offers training or entry level positions in the oil and gas i

We are needing a business card design for a new business called SKILLSTEP Industry training Inc. We are a training facility offering courses for entry level positions in the oil and gas industry. We like to keep the design in the colours of our logo. we like this also on the card "Get Prepared For A Flexible Career You Can Build On"

Industry/Entity Type

Oil And Gas

Contact Information for Business Card

Dorian Wexley
RR3 Site 9 Comp27
Cedarholm, NR, V2K8P3
250.418.5069 cell
250.418.7312 office
dorian@SKILLSTEPNORTH.ca
WWW.SKILLSTEPNORTH.CA

```html
<!DOCTYPE html>
<html lang="en">
<head>
<meta charset="utf-8">
<title>SKILLSTEP Industry Training Inc. – Business Card</title>
<link rel="stylesheet" href="https://fonts.googleapis.com/css2?family=Open+Sans:wght@400;600;700;800&display=swap">
<style>
  :root {
    --stage: #e9e9e9;
    --card: #ffffff;
    --card-back: #f3f3f2;
    --ink: #3a3a3a;
    --ink-soft: #4a4a4a;
    --red: #d62a22;
    --band-dark: #3c3c3c;
    --band-light: #f7f7f7;
    --ghost: #ececec;
  }
  * { box-sizing: border-box; margin: 0; padding: 0; }
  html, body {
    width: 1200px; height: 675px; overflow: hidden;
    background: var(--stage);
    font-family: "Open Sans", Arial, sans-serif;
    color: var(--ink);
  }
  .stage {
    position: relative; width: 1200px; height: 675px;
    display: flex; align-items: center; justify-content: center; gap: 50px;
  }
  .card {
    position: relative; width: 520px; height: 298px;
    overflow: hidden;
    box-shadow: 0 6px 18px rgba(0,0,0,.12);
  }
  .card--front { background: var(--card); }
  .card--back { background: var(--card-back); }

  .ghost-circle {
    position: absolute; border-radius: 50%;
    border: 34px solid var(--ghost);
  }
  .card--front .ghost-circle { width: 300px; height: 300px; right: -70px; top: -110px; }
  .card--back .ghost-circle { width: 260px; height: 260px; right: -60px; top: -90px; }

  .brand {
    position: absolute; display: flex; align-items: center; gap: 10px;
    color: var(--ink);
  }
  .brand__dot { flex: none; border-radius: 50%; background: var(--ink); }
  .brand__text { display: flex; flex-direction: column; line-height: 1; }
  .brand__name { font-weight: 800; letter-spacing: .5px; }
  .brand__sub { font-weight: 400; letter-spacing: 1.2px; margin-top: 6px; }

  .card--front .brand { left: 50%; top: 74px; transform: translateX(-50%); }
  .card--front .brand__dot { width: 40px; height: 40px; }
  .card--front .brand__name { font-size: 40px; }
  .card--front .brand__sub { font-size: 13px; }

  .card--back .brand { left: 30px; top: 120px; }
  .card--back .brand__dot { width: 26px; height: 26px; }
  .card--back .brand__name { font-size: 26px; }
  .card--back .brand__sub { font-size: 9px; }

  .front-bands { position: absolute; left: 0; bottom: 0; width: 520px; height: 110px; }

  .contact { position: absolute; left: 290px; top: 40px; width: 214px; }
  .contact__name { font-size: 16px; font-weight: 700; color: var(--ink); }
  .contact__role { font-size: 11px; font-weight: 400; color: var(--red); margin-top: 1px; }
  .contact__list { list-style: none; margin-top: 12px; font-size: 10.5px; color: var(--ink-soft); }
  .contact__list li { display: flex; align-items: center; gap: 7px; height: 17px; white-space: nowrap; }
  .contact__list svg { width: 11px; height: 11px; flex: none; fill: var(--red); }
  .contact__phones { gap: 12px !important; }
  .contact__phones span { display: inline-flex; align-items: center; gap: 6px; }
  .web-accent { color: var(--red); }
  .contact__rule { height: 2px; background: var(--red); margin: 8px -16px 8px 0; }
  .contact__address { display: flex; gap: 7px; font-size: 10.5px; line-height: 1.45; color: var(--ink-soft); }
  .contact__address svg { width: 11px; height: 13px; flex: none; fill: var(--red); margin-top: 2px; }

  .back-stripe { position: absolute; left: 0; right: 0; bottom: 0; height: 8px; background: var(--red); }
</style>
</head>
<body>
<main class="stage">

  <section class="card card--front" aria-label="Card front">
    <div class="ghost-circle"></div>
    <div class="brand">
      <span class="brand__dot"></span>
      <span class="brand__text">
        <span class="brand__name">SKILLSTEP</span>
        <span class="brand__sub">INDUSTRY TRAINING INC.</span>
      </span>
    </div>
    <svg class="front-bands" viewBox="0 0 520 110" preserveAspectRatio="none" aria-hidden="true">
      <polygon points="0,88 520,10 520,26 0,104" fill="var(--band-dark)"/>
      <polygon points="0,104 520,26 520,110 0,110" fill="var(--band-light)"/>
      <polygon points="0,92 258,53 276,59 0,110" fill="var(--red)"/>
    </svg>
  </section>

  <section class="card card--back" aria-label="Card back">
    <div class="ghost-circle"></div>
    <div class="brand">
      <span class="brand__dot"></span>
      <span class="brand__text">
        <span class="brand__name">SKILLSTEP</span>
        <span class="brand__sub">INDUSTRY TRAINING INC.</span>
      </span>
    </div>

    <div class="contact">
      <h1 class="contact__name">Dorian Wexley</h1>
      <p class="contact__role">Director</p>
      <ul class="contact__list">
        <li class="contact__phones">
          <span>
            <svg viewBox="0 0 12 12"><rect x="3" y="0" width="6" height="12" rx="1.2"/><rect x="4" y="1.5" width="4" height="7.5" fill="#fff"/></svg>
            250.418.5069
          </span>
          <span>
            <svg viewBox="0 0 12 12"><path d="M1 4c0-2 2-3 5-3s5 1 5 3l-2 1-1-1.5H4L3 5z"/><rect x="2" y="6" width="8" height="5" rx="1"/></svg>
            250.418.7312
          </span>
        </li>
        <li>
          <svg viewBox="0 0 12 12"><rect x="0" y="2" width="12" height="8"/><path d="M0 2l6 5 6-5" fill="none" stroke="#fff" stroke-width="1"/></svg>
          dorian@skillstepnorth.ca
        </li>
        <li>
          <svg viewBox="0 0 12 12"><circle cx="6" cy="6" r="5.5"/><path d="M.5 6h11M6 .5c-3 3-3 8 0 11M6 .5c3 3 3 8 0 11" fill="none" stroke="#fff" stroke-width=".8"/></svg>
          <span>www.<span class="web-accent">skillstepnorth</span>.ca</span>
        </li>
      </ul>
      <div class="contact__rule"></div>
      <p class="contact__address">
        <svg viewBox="0 0 12 14"><path d="M6 0a5 5 0 0 0-5 5c0 4 5 9 5 9s5-5 5-9a5 5 0 0 0-5-5z"/><circle cx="6" cy="5" r="2" fill="#fff"/></svg>
        <span>RR3 Site 9 Comp27 Cedarholm,<br>NR, V2K8P3</span>
      </p>
    </div>
    <div class="back-stripe"></div>
  </section>

</main>
</body>
</html>
```